Design a 1-page brochure with our "The Harborline Pathway" illustrated.

i have included my logo, an outline of the text and name of each step, and a quick sketch of generally how i would like the image to look. But please make it look sexy.

Each step should include the subtext as shown on the pdf attached. i.e. The first part of the image (far left) is "Problems", under that should list : 1. Poor Expectations; 2. Poor Communication... and so on for all the steps included.

I have also included a previous brochure that shows our branding and style.

Target Market(s)

Restaurant, Retail, Commercial

Industry/Entity Type

Construction Management

Font styles to use
Sans Serif

Colors
EB3D1F
EC4F4E
F09395
F8D3D4
FCEDEE

Requirements
Must have
• Our logo. Title of graphic: The Harborline Pathway, our website and IG. www.brevanbuildco.example. @brevanbuildco

```html
<!DOCTYPE html>
<html lang="en">
<head>
<meta charset="utf-8">
<title>The Harborline Pathway – Brevan Build Co</title>
<link rel="stylesheet" href="https://fonts.googleapis.com/css2?family=Montserrat:wght@700;800&family=Lato:wght@400;700&display=swap">
<style>
  :root {
    --red: #e8312a;
    --red-deep: #b3232a;
    --brand-red: #c8262c;
    --black: #000000;
    --ink: #111111;
    --white: #ffffff;
    --backdrop: #e6e7e9;
    --photo-dark: #1f2a2a;
    --photo-mid: #4a4a35;
    --photo-warm: #b0743a;
  }
  * { box-sizing: border-box; margin: 0; padding: 0; }
  html, body { width: 1003px; height: 1200px; overflow: hidden; background: var(--backdrop); }
  .brochure {
    position: absolute; left: 184px; top: 152px;
    width: 632px; height: 893px;
    background: var(--white);
    overflow: hidden;
    font-family: "Lato", sans-serif;
    color: var(--ink);
  }
  .brochure-shapes { position: absolute; inset: 0; }
  .brand {
    position: absolute; left: 34px; top: 136px;
    display: flex; align-items: center; gap: 8px;
  }
  .brand-mark { width: 12px; height: 12px; background: var(--red); }
  .brand-name {
    font-family: "Montserrat", sans-serif; font-weight: 800;
    font-size: 11px; letter-spacing: 0.2px; color: var(--white);
  }
  .title { position: absolute; left: 25px; top: 320px; font-weight: 800; }
  .title-kicker {
    display: block;
    font-family: "Montserrat", sans-serif; font-weight: 800;
    font-size: 17px; color: var(--brand-red); line-height: 18px;
  }
  .title-main {
    display: inline-block; min-width: 200px;
    font-family: "Montserrat", sans-serif; font-weight: 800;
    font-size: 33px; color: var(--black); line-height: 34px;
    padding-bottom: 3px; border-bottom: 1.5px solid var(--black);
    letter-spacing: 0.3px;
  }
  .problems { position: absolute; left: 28px; top: 394px; list-style: none; }
  .problems li, .step-points li {
    position: relative; padding-left: 12px;
    font-size: 13.5px; line-height: 17.6px;
  }
  .problems li::before, .step-points li::before {
    content: ""; position: absolute; left: 0; top: 6px;
    width: 5px; height: 5px; border-radius: 50%; background: var(--brand-red);
  }
  .divider {
    position: absolute; left: 59px; top: 512px; width: 514px;
    height: 2px; background: var(--brand-red);
  }
  .steps { position: absolute; left: 27px; top: 541px; list-style: none; }
  .step-name {
    font-family: "Montserrat", sans-serif; font-weight: 800;
    font-size: 19.5px; color: var(--brand-red);
    line-height: 22px; height: 26.6px;
    width: 124px; border-bottom: 1.5px solid var(--ink);
  }
  .step-name.wide { width: 140px; }
  .step-points { position: absolute; left: 176px; list-style: none; }
  .step-points .sep { display: inline-block; width: 1.5px; height: 15px; background: var(--brand-red); vertical-align: -2px; margin: 0 4px; }
  .step-points.small li { font-size: 11.5px; line-height: 14px; }
  .step-points.small li::before { top: 4.5px; }
  .contact {
    position: absolute; left: 344px; top: 811px;
    list-style: none; color: var(--white); font-size: 12.5px;
  }
  .contact li { display: flex; align-items: center; gap: 12px; height: 22px; }
  .contact svg { width: 13px; height: 13px; }
</style>
</head>
<body>
<main class="brochure">
  <svg class="brochure-shapes" width="632" height="893" viewBox="0 0 632 893">
    <defs>
      <linearGradient id="photo-tone" x1="0" y1="0" x2="1" y2="1">
        <stop offset="0" stop-color="var(--photo-dark)"/>
        <stop offset="0.45" stop-color="var(--photo-warm)"/>
        <stop offset="0.75" stop-color="var(--photo-mid)"/>
        <stop offset="1" stop-color="var(--photo-dark)"/>
      </linearGradient>
      <linearGradient id="red-fade" x1="0" y1="0" x2="1" y2="0">
        <stop offset="0" stop-color="var(--red)"/>
        <stop offset="1" stop-color="var(--red-deep)"/>
      </linearGradient>
    </defs>
    <polygon class="header-black" points="0,0 446,0 0,263" fill="var(--black)"/>
    <polygon class="header-stripe" points="446,0 501,0 0,288 0,263" fill="url(#red-fade)"/>
    <polygon class="hero-photo" role="img" aria-label="Aerial evening view of a lively outdoor retail and dining park with shipping-container buildings, string lights and a parking lot"
             points="501,0 632,0 632,445 130,213" fill="url(#photo-tone)"/>
    <polygon class="hero-wedge" points="96,248 130,213 632,445 632,513" fill="var(--black)"/>
    <polygon class="corner-red" points="0,680 226,793 0,793" fill="url(#red-fade)"/>
    <polygon class="footer-band" points="0,793 521,793 598,868 0,868" fill="var(--black)"/>
    <polygon class="footer-stripe" points="0,868 380,868 421,893 0,893" fill="url(#red-fade)"/>
  </svg>

  <div class="brand">
    <span class="brand-mark"></span>
    <span class="brand-name">BREVAN BUILD CO</span>
  </div>

  <h1 class="title">
    <span class="title-kicker">THE HARBORLINE</span>
    <span class="title-main">PATHWAY</span>
  </h1>

  <ul class="problems">
    <li>Common Problems</li>
    <li>Changing or poor expectations.</li>
    <li>Poor Communication</li>
    <li>No Journey To Success</li>
    <li>No Trust</li>
    <li>No Accountability</li>
  </ul>

  <div class="divider"></div>

  <ol class="steps">
    <li class="step-name">ORGANIZE</li>
    <li class="step-name">EXECUTE</li>
    <li class="step-name">MANAGE</li>
    <li class="step-name">COMPLETE</li>
    <li class="step-name wide">POSSIBILITY</li>
  </ol>

  <ul class="step-points" style="top:544px"><li>Develop Project Plan<span class="sep"></span>Develop Schedule<span class="sep"></span> Develop Budget</li></ul>
  <ul class="step-points" style="top:571px"><li>Project Start</li></ul>
  <ul class="step-points small" style="top:600px"><li>O.O.D.A<span class="sep"></span>Shared Consciousness Meetings<span class="sep"></span>Pressurized Collaboration</li></ul>
  <ul class="step-points small" style="top:627px"><li style="font-size:12.5px">Project Closeout</li></ul>
  <ul class="step-points small" style="top:651px">
    <li>Project Synergy</li>
    <li>Excellent Communication where Budget and Schedule are visible and approved.</li>
    <li>Clear project visibility where everyone understands how we get to a successful end.</li>
    <li>Everyone involved is proud of the final product.</li>
  </ul>

  <ul class="contact">
    <li>
      <svg viewBox="0 0 14 14"><rect x="1" y="3" width="12" height="8.5" fill="var(--red)"/><polyline points="1,3 7,8 13,3" fill="none" stroke="var(--black)" stroke-width="1.2"/></svg>
      <span>@brevanbuildco</span>
    </li>
    <li>
      <svg viewBox="0 0 14 14"><circle cx="7" cy="7" r="6" fill="var(--red)"/><g fill="none" stroke="var(--black)" stroke-width="0.9"><ellipse cx="7" cy="7" rx="2.6" ry="6"/><line x1="1" y1="7" x2="13" y2="7"/></g></svg>
      <span>www.brevanbuildco.example</span>
    </li>
  </ul>
</main>
</body>
</html>
```